PowerPoint Template for Calmont

Cover Page, Table of Contents Page, and slide template that can be incorporated into table of contents, in an editable form. Using attached logo.

```html
<!DOCTYPE html>
<html lang="en">
<head>
<meta charset="utf-8">
<title>Calmont Therapeutics – Presentation Template</title>
<link href="https://fonts.googleapis.com/css2?family=Open+Sans:wght@400;600;700&display=swap" rel="stylesheet">
<style>
:root{
  --bg-top:#b3eef0;
  --bg-bottom:#79d2da;
  --teal:#1aa3ad;
  --teal-dark:#13808a;
  --green:#7ab648;
  --light-blue:#a8d2de;
  --steel:#3a7f9c;
  --navy:#1f3b57;
  --title:#1c5f80;
  --text:#555d63;
  --muted:#8a9398;
  --band:#d5e7ed;
  --white:#ffffff;
}
*{margin:0;padding:0;box-sizing:border-box}
html,body{width:1200px;height:1200px;overflow:hidden}
body{font-family:"Open Sans",Arial,sans-serif;background:linear-gradient(180deg,var(--bg-top) 0%,var(--bg-bottom) 100%);position:relative;color:var(--text)}
.slide{position:absolute;width:380px;height:285px;background:linear-gradient(180deg,#eef9fa 0%,#ffffff 22%);box-shadow:0 2px 6px rgba(0,60,70,.18);overflow:hidden}
.s1{left:18px;top:158px}.s2{left:411px;top:158px}.s3{left:804px;top:158px}
.s4{left:18px;top:456px}.s5{left:411px;top:456px}.s6{left:804px;top:456px}
.s7{left:18px;top:753px}.s8{left:411px;top:753px}.s9{left:804px;top:753px}
.abs{position:absolute}
.slide-head{position:absolute;left:22px;top:22px;border-left:1.5px solid var(--teal);padding-left:8px;line-height:1.1}
.slide-title{font-size:12px;color:var(--title);font-weight:400}
.slide-sub{font-size:7.5px;color:#444}
.foot{position:absolute;left:18px;right:14px;top:262px;height:14px;display:flex;align-items:center;font-size:5.2px;color:var(--muted)}
.brand{font-size:10px;color:var(--teal);letter-spacing:1px;font-weight:400;display:flex;align-items:center;gap:3px}
.brand-dot{width:4px;height:4px;border-radius:50%;background:var(--green)}
.foot-doc{margin-left:10px}
.foot-doc b{color:#6a7378;font-weight:600}
.foot-web{margin-left:auto}
.foot-web b{color:#5a6368;font-weight:700}
.foot-page{border-left:1px solid #c5cdd0;margin-left:6px;padding-left:7px}
.small{font-size:5.4px;line-height:1.55;color:var(--text)}
.tiny{font-size:4.4px;line-height:1.55;color:var(--text)}
.just{text-align:justify}
.photo{position:absolute}
.hl{color:var(--teal);font-weight:700;font-size:7.5px}
.legend{display:flex;gap:7px;font-size:4.6px;color:#666}
.legend i{display:inline-block;width:4px;height:4px;margin-right:2px;vertical-align:-0.5px}
ul.dots{list-style:none}
ul.dots li{position:relative;padding-left:6px;margin-bottom:3px}
ul.dots li::before{content:"";position:absolute;left:0;top:2px;width:2.5px;height:2.5px;background:var(--teal)}
.member{position:absolute;width:72px;text-align:center}
.member-name{font-size:7.5px;color:var(--teal);margin-top:4px}
.member-role{font-size:4.5px;color:#777;margin-bottom:6px}
.member .tiny{text-align:justify}
.socials{display:flex;justify-content:center;gap:3px;margin-top:6px}
.socials span{width:10px;height:10px;border-radius:50%;background:var(--teal)}
.bar-label{position:absolute;top:224px;font-size:5.4px;color:#333;width:30px;text-align:center;font-weight:600}
.note{position:absolute;font-size:5.4px;color:#333;line-height:1.45}
.note b{font-weight:700}
.chart-cap{position:absolute;top:182px;width:70px;text-align:center}
.chart-cap h4{font-size:7px;color:var(--title);font-weight:700;margin-bottom:5px}
.service h3{font-size:8.5px;color:var(--title);font-weight:400}
.service ul{list-style:none;font-size:4.8px;color:#555;line-height:2.35}
.service li::before{content:"•";margin-right:4px;color:#777}
</style>
</head>
<body>

<!-- Slide 1: Bullet list with donut -->
<section class="slide s1">
  <div class="slide-head"><div class="slide-title">Bullet List Description</div><div class="slide-sub">Subtitle goes here</div></div>
  <svg class="abs" style="left:29px;top:62px" width="120" height="120" viewBox="0 0 120 120">
    <g transform="rotate(-90 60 60)" fill="none" stroke-width="18">
      <circle cx="60" cy="60" r="47" stroke="var(--green)" stroke-dasharray="59.06 295.31"/>
      <circle cx="60" cy="60" r="47" stroke="var(--teal)" stroke-dasharray="132.89 295.31" stroke-dashoffset="-59.06"/>
      <circle cx="60" cy="60" r="47" stroke="var(--light-blue)" stroke-dasharray="88.59 295.31" stroke-dashoffset="-191.95"/>
      <circle cx="60" cy="60" r="47" stroke="var(--steel)" stroke-dasharray="14.77 295.31" stroke-dashoffset="-280.54"/>
    </g>
    <g fill="#fff" font-size="7" font-family="Open Sans,sans-serif">
      <text x="86" y="28">20%</text><text x="72" y="102">45%</text><text x="3" y="56">30%</text><text x="44" y="15">5%</text>
    </g>
  </svg>
  <div class="abs tiny" style="left:28px;top:186px;width:120px;text-align:center;font-size:4.8px">Add Information Here<br>Sed ut perspiciatis unde omnis iste natus error sit voluptatem accusantium</div>
  <div class="abs" style="left:32px;top:216px;width:110px;border-top:1px solid #d8e4e8"></div>
  <div class="abs legend" style="left:35px;top:222px">
    <span><i style="background:var(--teal-dark)"></i>2014</span><span><i style="background:var(--steel)"></i>2014</span><span><i style="background:var(--light-blue)"></i>2014</span><span><i style="background:var(--green)"></i>2014</span>
  </div>
  <div class="abs" style="left:174px;top:78px;width:192px">
    <div style="font-size:7px;color:#333;line-height:1.45;margin-bottom:8px">Company Data in Particular Statistic Pie Chart<br>with Explanation</div>
    <p class="small" style="margin-bottom:8px">Sed ut perspiciatis unde omnis iste natus error sit voluptatem accusantium doloremque laudantium, totam rem aperiam, eaque ipsa quae ab illo inventore veritatis et quasi architecto beatae vitae dicta sunt explicabo. Nemo enim ipsam voluptatem quia voluptas sit aspernatur aut odit aut fugit, sed quia consequuntur magni dolores eos qui ratione voluptatem sequi nesciunt.</p>
    <ul class="dots tiny">
      <li>Lorem ipsum perspiciatis unde omnis iste natus sit voluptatem.<br>This description refer to the pie chart</li>
      <li>Perspiciatis unde omnis iste accusantium. This description refer to the pie chart</li>
      <li>Omnis iste natus sit voluptatem accusantium. Lorem ipsum perspiciatis unde<br>This description refer to the pie chart</li>
    </ul>
  </div>
  <footer class="foot"><span class="brand"><span class="brand-dot"></span>Calmont</span><span class="foot-doc"><b>Document for</b> Calmont Therapeutics</span><span class="foot-web">www.<b>calmont</b>therapeutics.com</span><span class="foot-page">04</span></footer>
</section>

<!-- Slide 2: Section title -->
<section class="slide s2" style="background:none">
  <div class="photo" role="img" aria-label="Radiotherapy treatment machine in a clinic, tinted teal" style="left:0;top:0;width:380px;height:285px;background:radial-gradient(ellipse at 65% 30%,#4fc3c6 0%,#24a7ad 40%,#137e88 100%)"></div>
  <svg class="abs" style="left:27px;top:123px" width="40" height="40"><circle cx="20" cy="20" r="19" fill="none" stroke="#fff" stroke-width="1"/><text x="20" y="26" text-anchor="middle" fill="#fff" font-size="16" font-family="Open Sans,sans-serif">01</text></svg>
  <div class="abs" style="left:84px;top:121px;color:#fff">
    <div style="font-size:19px;line-height:1.1">Section Title</div>
    <div style="font-size:5.2px;line-height:1.5;opacity:.9">Lorem ipsum dolor sit amet, consecteturi<br>magna aliqua dolce la vida loca olallaoye.</div>
  </div>
  <div class="abs" style="left:250px;top:124px;color:#fff;font-size:22px;letter-spacing:3px;display:flex;align-items:center;gap:6px"><span style="width:6px;height:6px;border-radius:50%;background:#fff"></span>Calmont</div>
</section>

<!-- Slide 3: Document slide -->
<section class="slide s3">
  <div class="slide-head"><div class="slide-title">Document Slide Title</div><div class="slide-sub">Subtitle goes here</div></div>
  <div class="photo" role="img" aria-label="Doctor holding a patient's hands, soft green tint" style="left:21px;top:55px;width:158px;height:112px;background:linear-gradient(135deg,#c7dc9a 0%,#a9cc86 50%,#e3edd0 100%)"></div>
  <div class="photo" role="img" aria-label="Radiotherapy machine above treatment table, blue tint" style="left:187px;top:55px;width:173px;height:112px;background:linear-gradient(135deg,#5fb3c6 0%,#8ccbd8 55%,#3f96ad 100%)"></div>
  <div class="abs" style="left:21px;top:181px;width:158px"><div class="hl">Highlighted Subtitle</div><p class="tiny just">Lorem ipsum dolor sit amet, consectetur adipiscing elit, sed do eiusmod tempor incididunt ut labore et dolore magna aliqua. Ut enim ad minim veniam, quis nostrud exercitation ullamco laboris nisi ut aliquip ex ea commodo consequat. Duis aute irure dolor in reprehenderit. Commodo consequat. Duis aute irure dolor in reprehenderit in voluptate velit esse cillum dolore eu fugiat nulla pariatur. Excepteur sint occaecat cupidatat non proident.</p></div>
  <div class="abs" style="left:187px;top:181px;width:173px"><div class="hl">Highlighted Subtitle</div><p class="tiny just">Lorem ipsum dolor sit amet, consectetur adipiscing elit, sed do eiusmod tempor incididunt ut labore et dolore magna aliqua. Ut enim ad minim veniam, quis nostrud exercitation ullamco laboris nisi ut aliquip ex ea commodo consequat. Duis aute dolor inreprehenderit. Commodo consequat. Duis aute irure dolor in reprehenderit in voluptate velit esse cillum dolore eu fugiat nulla pariatur. Excepteur sint occaecat cupidatat non proident.</p></div>
  <footer class="foot"><span class="brand"><span class="brand-dot"></span>Calmont</span><span class="foot-doc"><b>Document for</b> Calmont Therapeutics</span><span class="foot-web">www.<b>calmont</b>therapeutics.com</span><span class="foot-page">04</span></footer>
</section>

<!-- Slide 4: Team -->
<section class="slide s4">
  <div class="slide-head"><div class="slide-title">Our Team</div><div class="slide-sub">Subtitle goes here</div></div>
  <div class="member" style="left:28px;top:72px">
    <div role="img" aria-label="Portrait photo of team member" style="width:64px;height:64px;margin:0 auto;border-radius:50%;background:linear-gradient(160deg,#d8e8f2,#8fb4cc);box-shadow:0 0 0 1.5px #fff,0 0 0 2.5px var(--light-blue)"></div>
    <div class="member-name">Nora Vale</div><div class="member-role">Founding Member</div>
    <p class="tiny">Lorem Ipsum has been the dummy text and can be replaced with your original text here regarding to this person's description</p>
    <div class="socials"><span></span><span></span><span></span></div>
  </div>
  <div class="member" style="left:114px;top:72px">
    <div role="img" aria-label="Portrait photo of team member" style="width:64px;height:64px;margin:0 auto;border-radius:50%;background:linear-gradient(160deg,#e8eef2,#a8bfcc);box-shadow:0 0 0 1.5px #fff,0 0 0 2.5px var(--light-blue)"></div>
    <div class="member-name">Jane Doe</div><div class="member-role">Founding Member</div>
    <p class="tiny">Lorem Ipsum has been the dummy text and can be replaced with your original text here regarding to this person's description</p>
    <div class="socials"><span></span><span></span><span></span></div>
  </div>
  <div class="member" style="left:199px;top:72px">
    <div role="img" aria-label="Portrait photo of team member" style="width:64px;height:64px;margin:0 auto;border-radius:50%;background:linear-gradient(160deg,#b9a894,#4a4a4e);box-shadow:0 0 0 1.5px #fff,0 0 0 2.5px var(--light-blue)"></div>
    <div class="member-name">Owen Hale</div><div class="member-role">Founding Member</div>
    <p class="tiny">Lorem Ipsum has been the dummy text and can be replaced with your original text here regarding to this person's description</p>
    <div class="socials"><span></span><span></span><span></span></div>
  </div>
  <div class="member" style="left:282px;top:72px">
    <div role="img" aria-label="Portrait photo of team member" style="width:64px;height:64px;margin:0 auto;border-radius:50%;background:linear-gradient(160deg,#d9d9d9,#7b7f84);box-shadow:0 0 0 1.5px #fff,0 0 0 2.5px var(--light-blue)"></div>
    <div class="member-name">Julian Reyes</div><div class="member-role">Founding Member</div>
    <p class="tiny">Lorem Ipsum has been the dummy text and can be replaced with your original text here regarding to this person's description</p>
    <div class="socials"><span></span><span></span><span></span></div>
  </div>
  <footer class="foot"><span class="brand"><span class="brand-dot"></span>Calmont</span><span class="foot-doc"><b>Document for</b> Calmont Therapeutics</span><span class="foot-web">www.<b>calmont</b>therapeutics.com</span><span class="foot-page">04</span></footer>
</section>

<!-- Slide 5: Bar chart -->
<section class="slide s5">
  <div class="slide-head"><div class="slide-title">Bar Chart</div><div class="slide-sub">Subtitle goes here</div></div>
  <svg class="abs" style="left:0;top:0" width="380" height="285">
    <g stroke="#c9d3d6" stroke-width=".6">
      <line x1="48" y1="104" x2="48" y2="150"/><line x1="170" y1="120" x2="170" y2="193"/><line x1="251" y1="162" x2="251" y2="202"/><line x1="333" y1="128" x2="333" y2="184"/>
    </g>
    <rect x="40" y="150" width="16" height="70" fill="var(--teal)"/>
    <rect x="81" y="150" width="16" height="70" fill="var(--teal)"/>
    <rect x="122" y="158" width="16" height="62" fill="var(--light-blue)"/>
    <rect x="162" y="193" width="16" height="27" fill="var(--light-blue)"/>
    <rect x="203" y="186" width="16" height="34" fill="var(--light-blue)"/>
    <rect x="243" y="202" width="16" height="18" fill="var(--light-blue)"/>
    <rect x="284" y="205" width="16" height="15" fill="var(--green)"/>
    <rect x="325" y="184" width="16" height="36" fill="var(--green)"/>
  </svg>
  <div class="note" style="left:40px;top:84px"><b>Month :</b> Name it<br><b>Total Profit :</b> $ 10,000,000</div>
  <div class="note" style="left:126px;top:103px"><b>Month :</b> Name it<br><b>Total Profit :</b> $ 10,000,000</div>
  <div class="note" style="left:274px;top:100px;text-align:right"><b>Month :</b> Name it<br><b>Total Profit :</b> $ 10,000,000</div>
  <div class="note" style="left:241px;top:148px"><b>Month :</b> Name it<br><b>Total Profit :</b> $ 10,000,000</div>
  <span class="bar-label" style="left:33px">VAR A</span><span class="bar-label" style="left:74px">VAR B</span><span class="bar-label" style="left:115px">VAR C</span><span class="bar-label" style="left:155px">VAR D</span><span class="bar-label" style="left:196px">VAR E</span><span class="bar-label" style="left:236px">VAR F</span><span class="bar-label" style="left:277px">VAR G</span><span class="bar-label" style="left:318px">VAR H</span>
  <footer class="foot"><span class="brand"><span class="brand-dot"></span>Calmont</span><span class="foot-doc"><b>Document for</b> Calmont Therapeutics</span><span class="foot-web">www.<b>calmont</b>therapeutics.com</span><span class="foot-page">04</span></footer>
</section>

<!-- Slide 6: Ring charts -->
<section class="slide s6">
  <div class="slide-head"><div class="slide-title">Chart</div><div class="slide-sub">Subtitle goes here</div></div>
  <svg class="abs" style="left:0;top:68px" width="380" height="106">
    <rect x="0" y="0" width="380" height="100" fill="var(--band)"/>
    <polygon points="79,100 87,100 83,105" fill="var(--band)"/><polygon points="186,100 194,100 190,105" fill="var(--band)"/><polygon points="293,100 301,100 297,105" fill="var(--band)"/>
    <g fill="none">
      <circle cx="83" cy="50" r="28" stroke="var(--navy)" stroke-width="2"/>
      <circle cx="83" cy="50" r="28" stroke="var(--teal)" stroke-width="3.5" stroke-dasharray="72.1 175.9" transform="rotate(-90 83 50)"/>
      <circle cx="190" cy="50" r="28" stroke="var(--navy)" stroke-width="2"/>
      <circle cx="190" cy="50" r="28" stroke="var(--teal)" stroke-width="3.5" stroke-dasharray="131.9 175.9" transform="rotate(-90 190 50)"/>
      <circle cx="297" cy="50" r="28" stroke="var(--navy)" stroke-width="2"/>
      <circle cx="297" cy="50" r="28" stroke="var(--teal)" stroke-width="3.5" stroke-dasharray="87.9 175.9" transform="rotate(-90 297 50)"/>
    </g>
    <circle cx="55" cy="54" r="3" fill="var(--teal)"/><circle cx="210" cy="30" r="3" fill="var(--navy)"/><circle cx="325" cy="50" r="3" fill="var(--teal)"/>
    <g fill="var(--navy)" font-size="12" font-weight="700" font-family="Open Sans,sans-serif" text-anchor="middle">
      <text x="83" y="54">41%</text><text x="190" y="54">75%</text><text x="297" y="54">50%</text>
    </g>
  </svg>
  <div class="chart-cap" style="left:48px"><h4>/ Chart 01</h4><p class="tiny just">Lorem Ipsum has been the dummy text and can be replaced with your original text here regarding to this person's description</p></div>
  <div class="chart-cap" style="left:155px"><h4>/ Chart 02</h4><p class="tiny just">Lorem Ipsum has been the dummy text and can be replaced with your original text here regarding to this person's description</p></div>
  <div class="chart-cap" style="left:262px"><h4>/ Chart 03</h4><p class="tiny just">Lorem Ipsum has been the dummy text and can be replaced with your original text here regarding to this person's description</p></div>
  <footer class="foot"><span class="brand"><span class="brand-dot"></span>Calmont</span><span class="foot-doc"><b>Document for</b> Calmont Therapeutics</span><span class="foot-web">www.<b>calmont</b>therapeutics.com</span><span class="foot-page">04</span></footer>
</section>

<!-- Slide 7: Image left -->
<section class="slide s7">
  <div class="slide-head"><div class="slide-title">Image Left</div><div class="slide-sub">Subtitle goes here</div></div>
  <div class="photo" role="img" aria-label="Physiotherapist examining a patient's knee" style="left:0;top:64px;width:210px;height:151px;background:linear-gradient(135deg,#f3f5f6 0%,#e6d7cc 50%,#f7f8f9 100%)"></div>
  <div class="abs" style="left:219px;top:64px;width:144px">
    <div style="font-size:9.5px;color:#333;margin-bottom:4px">Highlighted Subtitle</div>
    <p class="small just">Maecenas sed diam eget risus varius blandit sit amet non magna. Donec id elit non mi porta gravida at eget metus. Maecenas sed diam eget risus varius blandit sit amet non magna. Maecenas sed diam eget risus varius blandit sit amet non magna. Donec id elit non mi porta gravida at eget metus. Maecenas sed diam eget risus varius blandit sit amet non magna. Maecenas sed diam eget risus varius blandit sit amet Donec id elit non mi porta gravida at eget metus. Maecenas sed diam eget risus varius blandit sit amet non magna. Maecenas sed diam eget risus varius blandit sit amet Donec id elit non mi porta gravida at eget metus. Maecenas sed diam eget risus varius</p>
  </div>
  <footer class="foot"><span class="brand"><span class="brand-dot"></span>Calmont</span><span class="foot-doc"><b>Document for</b> Calmont Therapeutics</span><span class="foot-web">www.<b>calmont</b>therapeutics.com</span><span class="foot-page">04</span></footer>
</section>

<!-- Slide 8: Image right -->
<section class="slide s8">
  <div class="slide-head"><div class="slide-title">Image Right</div><div class="slide-sub">Subtitle goes here</div></div>
  <div class="abs" style="left:27px;top:64px;width:144px">
    <div style="font-size:9.5px;color:#333;margin-bottom:4px">Highlighted Subtitle</div>
    <p class="small just">Maecenas sed diam eget risus varius blandit sit amet non magna. Donec id elit non mi porta gravida at eget metus. Maecenas sed diam eget risus varius blandit sit amet non magna. Maecenas sed diam eget risus varius blandit sit amet non magna. Donec id elit non mi porta gravida at eget metus. Maecenas sed diam eget risus varius blandit sit amet non magna. Maecenas sed diam eget risus varius blandit sit amet Donec id elit non mi porta gravida at eget metus. Maecenas sed diam eget risus varius blandit sit amet non magna. Maecenas sed diam eget risus varius blandit sit amet Donec id elit non mi porta gravida at eget metus. Maecenas sed diam eget risus varius</p>
  </div>
  <div class="photo" role="img" aria-label="Doctor consulting with a patient at a desk" style="left:179px;top:64px;width:201px;height:151px;background:linear-gradient(135deg,#eef4f7 0%,#dfe9ee 50%,#f6ece4 100%)"></div>
  <footer class="foot"><span class="brand"><span class="brand-dot"></span>Calmont</span><span class="foot-doc"><b>Document for</b> Calmont Therapeutics</span><span class="foot-web">www.<b>calmont</b>therapeutics.com</span><span class="foot-page">04</span></footer>
</section>

<!-- Slide 9: Competencies -->
<section class="slide s9">
  <div class="slide-head"><div class="slide-title">CALMONT Therapeutics Core Competencies</div><div class="slide-sub">Subtitle goes here</div></div>
  <div class="abs service" style="left:28px;top:71px">
    <div style="display:flex;align-items:center;gap:6px">
      <svg width="24" height="24"><circle cx="12" cy="12" r="12" fill="var(--teal)"/><circle cx="10" cy="9" r="3" fill="#fff"/><path d="M5 18c0-3 2-5 5-5s5 2 5 5z" fill="#fff"/><rect x="14" y="7" width="5" height="4" rx="1" fill="#fff"/></svg>
      <h3>Consulting Services</h3>
    </div>
    <ul style="margin:2px 0 0 30px">
      <li>Acquisition Support Services</li><li>Program/ Project/ Portfolio</li><li>Management</li><li>Financial Management</li><li>Business Process Re-engineering</li><li>Administrative Support System Engineering</li><li>Logistics Management</li>
    </ul>
  </div>
  <div class="abs service" style="left:179px;top:71px">
    <div style="display:flex;align-items:center;gap:6px">
      <svg width="24" height="24"><circle cx="12" cy="12" r="12" fill="var(--green)"/><rect x="6" y="7" width="12" height="8" rx="1" fill="none" stroke="#fff" stroke-width="1.3"/><rect x="9" y="16" width="6" height="1.5" fill="#fff"/></svg>
      <h3>Technology Services</h3>
    </div>
    <ul style="margin:2px 0 0 30px">
      <li>Enterprise Portal Solution</li><li>Web Application Development</li><li>Cloud Integration Technology</li><li>Acquisition IT Modernization</li><li>User Experience (UX) Focused Design</li><li>Service Oriented Architecture (SOA)</li><li>Cyber Security and Software QA</li><li>Business Intelligence (BI) Architecture and Engineering</li><li>Edge Content Delivery Network (CDN)</li><li>Service and Cloud Security Reseller</li>
    </ul>
  </div>
  <footer class="foot"><span class="brand"><span class="brand-dot"></span>Calmont</span><span class="foot-doc"><b>Document for</b> Calmont Therapeutics</span><span class="foot-web">www.<b>calmont</b>therapeutics.com</span><span class="foot-page">04</span></footer>
</section>

</body>
</html>
```